TheMarlowVault.com web site

We need a Wordpress theme for a new business we are launching called:

TheMarlowVault.com

"Real time access to currency markets for eCommerce"

You can see the logo / colours at www.themarlowvault.com (the logo was designed by a PixelHarbor.com designer!).

Web site to be along simlar lines to our pre-launch site www.themarlowvault.com

The marlow vault is a fintech / financial services company (i.e. the DNA is more tech than financial services) that has three products:

1. SaaS Ledger Tools - that customers can use to run their own currency business

2. PaaS Ledger Link - that customers use to develop their own currency apps and / or integrate currency capabilities into their existing apps and processes

3. Ledger Flow - direct access to the currency markets to buy/sell currency and make international payments. Forex rates are transparent, consistent and fair for all customers.

Other notes...

A more web 2.0'ish / API related brand, but still serious enough to be take seriously be CxO level decision makers.

The brand is B2B and not B2C or C2C

Please do NOT put forward canned designs found at places like layoutbarnyard.com etc.

Reason: Hi,

We have increased the budget for this project - please take another look.

Regards,

Gareth

Hi,

The logo .png file has been uploaded to the design brief

Gareth

Hi,

Some feedback based on what as been submitted so far..

- the logo is designed to go on white background

- take a closer look at our existing "hacked together" site www.themarlowvault.com (we like this)- take a look at the site of our owner www.brightwelltrust.co.uk- you will notice the sleek, un-cluttered and professional designKindest regards,Gareth

Reason: Just so we get the finishing touches done

Target Market(s)

B2B Targets three main communities:

- financial decision makers
- product managers
- technology/ developer community (for our APIs)

Industry/Entity Type

Financial

Requirements
Must have
• Not appear to be a "blog", but a simple to manage a web site based upon a wordpress theme.

Sections for "product", "blog", "about us", "products"

Clear "call to action" buttons (contact us, sign up etc.) and social buttons

Front page to have a space for video content (as per current web site)

Must have a clear section on the front page "what can we do for you?" where we list various client types and how we can help them

Must have a clear section on the front page "what we do?" where we list the various services we do

```html
<!DOCTYPE html>
<html lang="en">
<head>
<meta charset="utf-8">
<title>TheMarlowVault.com</title>
<link rel="stylesheet" href="https://fonts.googleapis.com/css2?family=Arimo:wght@400&display=swap">
<style>
:root{
  --brand-blue:#5085a5;
  --nav-active:#2f5f7c;
  --rule-light:#a8c3d3;
  --text-grey:#5b5b5b;
  --heading-grey:#4f4f4f;
  --divider:#cfcfcf;
  --white:#ffffff;
  --logo-grey:#595656;
  --logo-blue:#6cbde8;
  --player-black:#000000;
  --player-bar:#b9b9b9;
}
*{margin:0;padding:0;box-sizing:border-box}
html,body{width:1126px;height:1200px;overflow:hidden;background:var(--white)}
body{position:relative;font-family:"Arimo",Arial,sans-serif;color:var(--text-grey)}
.abs{position:absolute}

/* header */
.site-header{left:0;top:0;width:1126px;height:123px;background:var(--white)}
.brand{left:20px;top:58px;display:flex;align-items:center;gap:10px}
.brand-dot{width:26px;height:26px;border-radius:50%;background:var(--logo-blue)}
.brand-name{font-size:29px;color:var(--logo-grey);letter-spacing:-.3px;white-space:nowrap}

/* hero band */
.hero{left:0;top:123px;width:1126px;height:320px;background:var(--brand-blue)}
.main-nav a,.cta-nav a{position:absolute;color:var(--white);text-decoration:none;font-size:16px;white-space:nowrap}
.main-nav a{top:35px;line-height:21px}
.main-nav a.is-active{background:var(--nav-active);padding:0 10px;margin-left:-10px}
.hero-rule{left:20px;top:84px;width:1075px;height:1px;background:var(--rule-light)}
.cta-nav a{top:71px;line-height:20px;padding:0 2px;background:var(--brand-blue)}

.video-player{left:437px;top:95px;width:274px;height:225px;background:var(--player-black)}
.video-controls{left:0;bottom:0;width:274px;height:18px;background:linear-gradient(#dcdcdc,var(--player-bar))}

/* content */
.col h2{font-weight:400;font-size:21px;color:var(--heading-grey);line-height:24px}
.col p{margin-top:9px;margin-left:2px;font-size:15.8px;line-height:19.05px;color:var(--text-grey);white-space:nowrap}
.col-left{left:95px;top:556px}
.col-right{left:640px;top:556px}
.col-divider{left:580px;top:553px;width:2px;height:342px;background:var(--divider)}

/* footer */
.site-footer{left:0;top:1066px;width:1126px;height:134px;background:var(--brand-blue);color:var(--white)}
.foot-col h3{font-weight:400;font-size:16px;line-height:19px}
.foot-col p{font-size:10.3px;line-height:12.8px;white-space:nowrap}
.foot-sep{top:16px;width:1px;height:90px;background:rgba(255,255,255,.18)}
.social{top:40px;left:794px;display:flex}
.social span{display:block;width:37px;height:37px;border-radius:5px;margin-right:5px}
.foot-rule{left:88px;top:116px;width:945px;height:1px;background:var(--rule-light)}
.copyright{left:0;top:121px;width:1126px;text-align:center;font-size:10.5px;line-height:12px}
</style>
</head>
<body>

<header class="site-header abs">
  <div class="brand abs">
    <span class="brand-dot"></span>
    <span class="brand-name">TheMarlowVault.com</span>
  </div>
</header>

<section class="hero abs">
  <nav class="main-nav">
    <a class="is-active" href="#" style="left:688px">Home</a>
    <a href="#" style="left:758px">Product</a>
    <a href="#" style="left:837px">Blog</a>
    <a href="#" style="left:890px">About Us</a>
    <a href="#" style="left:978px">Products</a>
  </nav>
  <div class="hero-rule abs"></div>
  <nav class="cta-nav">
    <a href="#" style="left:766px">call to action...</a>
    <a href="#" style="left:916px">contact us</a>
    <a href="#" style="left:1030px">sign up</a>
  </nav>

  <div class="video-player abs">
    <svg class="abs" style="left:129px;top:99px" width="16" height="16" viewBox="0 0 16 16">
      <g fill="#8a8a8a">
        <circle cx="8" cy="2" r="1.6"/><circle cx="12.2" cy="3.8" r="1.4" opacity=".85"/>
        <circle cx="14" cy="8" r="1.3" opacity=".75"/><circle cx="12.2" cy="12.2" r="1.2" opacity=".65"/>
        <circle cx="8" cy="14" r="1.2" opacity=".55"/><circle cx="3.8" cy="12.2" r="1.2" opacity=".45"/>
        <circle cx="2" cy="8" r="1.3" opacity=".9"/><circle cx="3.8" cy="3.8" r="1.4"/>
      </g>
    </svg>
    <svg class="video-controls abs" viewBox="0 0 274 18" width="274" height="18">
      <rect x="3" y="4" width="3" height="9" fill="#444"/><rect x="8" y="4" width="3" height="9" fill="#444"/>
      <rect x="22" y="4" width="2" height="9" fill="#444"/><path d="M31 4v9l-7-4.5z" fill="#444"/>
      <circle cx="42" cy="8.5" r="3.5" fill="#555"/><rect x="46" y="7.5" width="93" height="2" fill="#333"/>
      <rect x="143" y="3" width="50" height="11" fill="#111"/>
      <text x="146" y="11" font-size="6" fill="#ddd" font-family="Arimo,sans-serif">00:00 / <tspan fill="#e33">01:47</tspan></text>
      <rect x="208" y="7.5" width="28" height="2" fill="#333"/><rect x="237" y="5" width="2" height="7" fill="#333"/>
      <path d="M243 7h3l4-3v10l-4-3h-3z" fill="#444"/>
      <rect x="254" y="5" width="8" height="7" fill="none" stroke="#444"/><rect x="264" y="5" width="8" height="7" fill="none" stroke="#444"/>
    </svg>
  </div>
</section>

<section class="col col-left abs">
  <h2>what can we do for you ?</h2>
  <p>Lorem ipsum dolor sit amet, consectetur adipi-<br>scing elit. Aliquam varius pellentesque venenatis.<br>Aliquam dignissim, urna eget mattis tincidunt,<br>justo felis tincidunt tortor, non pulvinar lectus nibh<br>eu diam. Ut nec mauris sed orci porta congue.<br>Vestibulum consectetur nisi ac neque ultricies<br>scelerisque. Nullam dictum pellentesque turpis,<br>volutpat tempor diam interdum id. Vestibulum<br>sed dui nunc, eget posuere orci. Aenean sollicitu-<br>din ipsum sed purus auctor sit amet vehicula<br>tortor cursus. Vivamus nec neque sed purus frin-<br>gilla pharetra quis eu leo. Etiam ullamcorper<br>nunc sit amet felis ornare pretium. Maecenas<br>posuere tincidunt nunc, lacinia scelerisque tortor<br>suscipit in. Nunc sed augue metus. Duis ac felis</p>
</section>

<div class="col-divider abs"></div>

<section class="col col-right abs">
  <h2>what we do ?</h2>
  <p>Lorem ipsum dolor sit amet, consectetur adipi-<br>scing elit. Aliquam varius pellentesque venenatis.<br>Aliquam dignissim, urna eget mattis tincidunt,<br>justo felis tincidunt tortor, non pulvinar lectus nibh<br>eu diam. Ut nec mauris sed orci porta congue.<br>Vestibulum consectetur nisi ac neque ultricies<br>scelerisque. Nullam dictum pellentesque turpis,<br>volutpat tempor diam interdum id. Vestibulum<br>sed dui nunc, eget posuere orci. Aenean sollicitu-<br>din ipsum sed purus auctor sit amet vehicula<br>tortor cursus. Vivamus nec neque sed purus frin-<br>gilla pharetra quis eu leo. Etiam ullamcorper<br>nunc sit amet felis ornare pretium. Maecenas<br>posuere tincidunt nunc, lacinia scelerisque tortor<br>suscipit in. Nunc sed augue metus. Duis ac felis</p>
</section>

<footer class="site-footer abs">
  <div class="foot-col abs" style="left:94px;top:10px">
    <h3>About Us</h3>
    <p>Lorem ipsum dolor sit amet, consectetur adipiscing elit. Aliquam<br>varius pellentesque venenatis. Aliquam dignissim, urna eget mattis<br>tincidunt, justo felis tincidunt tortor, non pulvinar lectus nibh eu<br>diam. Ut nec mauris sed orci porta congue. Vestibulum consectetur<br>nisi ac neque ultricies scelerisque. Nullam dictum pellentesque<br>turpis, volutpat tempor diam interdum id. Vestibulum sed dui nunc,<br>eget posuere orci. Aenean sollicitudin ipsum sed purus auctor sit</p>
  </div>
  <div class="foot-sep abs" style="left:427px"></div>
  <div class="foot-col abs" style="left:446px;top:10px">
    <h3>Support</h3>
    <p>Lorem ipsum dolor sit amet, consectetur adipiscing elit. Aliquam<br>varius pellentesque venenatis. Aliquam dignissim, urna eget mattis<br>tincidunt, justo felis tincidunt tortor, non pulvinar lectus nibh eu<br>diam. Ut nec mauris sed orci porta congue. Vestibulum consectetur<br>nisi ac neque ultricies scelerisque. Nullam dictum pellentesque<br>turpis, volutpat tempor diam interdum id. Vestibulum sed dui nunc,<br>eget posuere orci. Aenean sollicitudin ipsum sed purus auctor sit</p>
  </div>
  <div class="foot-sep abs" style="left:779px"></div>
  <div class="foot-col abs" style="left:798px;top:10px">
    <h3>Connect</h3>
  </div>
  <div class="social abs">
    <span role="img" aria-label="Feed link" style="background:#f0913a"></span>
    <span role="img" aria-label="Chat link" style="background:#2ea8e0"></span>
    <span role="img" aria-label="Updates link" style="background:#8fc7cf"></span>
    <span role="img" aria-label="Profile link" style="background:#5aa150"></span>
    <span role="img" aria-label="Community link" style="background:#4a68a8"></span>
  </div>
  <div class="foot-rule abs"></div>
  <p class="copyright abs">Copyright 2011 MarlowVault. All right reserved.</p>
</footer>

</body>
</html>
```